Email Signatures

I would like to create a new email signature for my team. The design will be the same for everyone, with only individual details such as name and email changing. You can also see our brand style on our website. https://www.tlmbespokehomes.com.au/

Target Market(s)

Clients for new builds or renovations

Industry/Entity Type

Construction

Colors

Designer to choose colors to be used in the design.

```html
<!DOCTYPE html>
<html lang="en">
<head>
<meta charset="utf-8">
<title>TLM Bespoke Homes – Email Signature</title>
<link rel="stylesheet" href="https://fonts.googleapis.com/css2?family=Roboto:wght@300;400;700;900&display=swap">
<style>
  :root {
    --brand-green: #159a3c;
    --tint-green: #e3f4e8;
    --tint-green-fade: #f4fbf6;
    --ink: #333538;
    --ink-soft: #4a4c50;
    --rule: #8a8c90;
    --paper: #ffffff;
    --portrait-light: #e4e6e8;
    --portrait-mid: #b9bcc0;
    --portrait-dark: #2a2c30;
  }
  * { box-sizing: border-box; margin: 0; padding: 0; }
  html, body {
    width: 1200px;
    height: 384px;
    overflow: hidden;
    background: var(--paper);
  }
  .signature {
    position: relative;
    width: 1200px;
    height: 384px;
    background: var(--paper);
    font-family: "Roboto", Arial, sans-serif;
    color: var(--ink);
  }
  .brand-name {
    position: absolute;
    left: 34px;
    top: 26px;
    font-size: 46px;
    font-weight: 900;
    letter-spacing: 2px;
    color: var(--ink);
    line-height: 1;
  }
  .person-name {
    position: absolute;
    left: 32px;
    top: 118px;
    font-size: 48px;
    font-weight: 400;
    line-height: 48px;
    color: var(--ink);
  }
  .person-role {
    position: absolute;
    left: 34px;
    top: 220px;
    font-size: 23px;
    font-weight: 400;
    color: var(--ink-soft);
  }
  .social-links {
    position: absolute;
    left: 36px;
    top: 280px;
    display: flex;
    gap: 22px;
  }
  .social-link {
    display: flex;
    align-items: center;
    gap: 7px;
    font-size: 17px;
    font-weight: 400;
    color: var(--ink-soft);
    text-decoration: none;
  }
  .social-dot {
    width: 14px;
    height: 14px;
    border: 2px solid var(--ink);
    border-radius: 50%;
    flex: none;
  }
  .divider {
    position: absolute;
    left: 285px;
    top: 124px;
    width: 2px;
    height: 192px;
    background: var(--rule);
  }
  .contact-list {
    position: absolute;
    left: 334px;
    top: 142px;
    list-style: none;
  }
  .contact-item {
    display: flex;
    align-items: center;
    height: 44px;
    margin-bottom: 10px;
    font-size: 25px;
    font-weight: 400;
    color: var(--ink-soft);
  }
  .contact-item a {
    color: inherit;
    text-decoration: none;
  }
  .contact-icon {
    width: 30px;
    height: 30px;
    margin-right: 12px;
    flex: none;
  }
  .accent-tint {
    position: absolute;
    left: 770px;
    top: 16px;
    width: 96px;
    height: 84px;
    background: linear-gradient(135deg, var(--tint-green) 0%, var(--tint-green-fade) 100%);
  }
  .accent-block {
    position: absolute;
    left: 876px;
    top: 16px;
    width: 304px;
    height: 304px;
    background: var(--brand-green);
  }
  .portrait {
    position: absolute;
    left: 832px;
    top: 56px;
    width: 308px;
    height: 312px;
    background:
      linear-gradient(180deg, transparent 55%, var(--portrait-dark) 100%),
      linear-gradient(120deg, var(--portrait-light) 0%, var(--portrait-mid) 100%);
  }
</style>
</head>
<body>
  <div class="signature">
    <div class="brand-name">TLM</div>

    <h1 class="person-name">Liam<br>Hartley</h1>
    <p class="person-role">General Manager</p>

    <nav class="social-links" aria-label="Social profiles">
      <a class="social-link" href="#"><span class="social-dot"></span>Profile</a>
      <a class="social-link" href="#"><span class="social-dot"></span>Videos</a>
    </nav>

    <div class="divider"></div>

    <ul class="contact-list">
      <li class="contact-item">
        <svg class="contact-icon" viewBox="0 0 30 30" fill="none" stroke="#159a3c" stroke-width="2.2" stroke-linejoin="round">
          <rect x="3" y="7" width="24" height="17" rx="1.5"/>
          <path d="M3.5 8 L15 17 L26.5 8"/>
        </svg>
        liam@tlmbespokehomes.com.au
      </li>
      <li class="contact-item">
        <svg class="contact-icon" viewBox="0 0 30 30" fill="none" stroke="#159a3c" stroke-width="2.2" stroke-linejoin="round">
          <path d="M8 4 L12 4 L14 10 L11 12.5 C12.5 16 14 17.5 17.5 19 L20 16 L26 18 L26 22 C26 24 24 26 22 26 C13 25.5 4.5 17 4 8 C4 6 6 4 8 4 Z"/>
          <path d="M18 4.5 A8 8 0 0 1 25.5 12"/>
          <path d="M18 9 A3.5 3.5 0 0 1 21 12"/>
        </svg>
        9731552048
      </li>
      <li class="contact-item">
        <svg class="contact-icon" viewBox="0 0 30 30" fill="none" stroke="#159a3c" stroke-width="2.2">
          <circle cx="15" cy="15" r="11.5"/>
          <ellipse cx="15" cy="15" rx="5" ry="11.5"/>
          <path d="M3.5 15 H26.5 M5.5 9 H24.5 M5.5 21 H24.5"/>
        </svg>
        <a href="https://www.tlmbespokehomes.com.au/">tlmbespokehomes.com.au/</a>
      </li>
    </ul>

    <div class="accent-tint" role="img" aria-label="Light green decorative texture"></div>
    <div class="accent-block"></div>
    <div class="portrait" role="img" aria-label="Portrait photo of Liam Hartley, General Manager, in a dark company polo shirt"></div>
  </div>
</body>
</html>
```